Tallgrove Vale Management

I need a professional website. My current website is tallgrovevalemanagement.com and I hate it. It was created with some AI tool very quickly because I needed a site up and running with no advanced notice. I’m open to all designs .. I trust you, the professionals will deliver the results I’m anxiously awaiting! :)

```html
<!DOCTYPE html>
<html lang="en">
<head>
<meta charset="utf-8">
<title>Tallgrove Vale Management</title>
<link rel="stylesheet" href="https://fonts.googleapis.com/css2?family=Figtree:ital,wght@0,400;0,500;0,600;0,700;1,400;1,500&display=swap">
<style>
:root{
  --navy:#0e1a2c;
  --navy-2:#13233a;
  --footer:#111b29;
  --blue:#1c6ae0;
  --blue-dark:#1558c0;
  --ink:#141a24;
  --body:#4b5563;
  --muted:#6b7280;
  --line:#e5e8ee;
  --soft:#f3f5f9;
  --white:#ffffff;
}
*{box-sizing:border-box;margin:0;padding:0}
html,body{width:1200px;height:3001px;overflow:hidden}
body{font-family:"Figtree",Arial,sans-serif;color:var(--ink);background:var(--white);position:relative}
a{color:inherit;text-decoration:none}
.abs{position:absolute}

/* Header */
.site-header{position:absolute;left:0;top:0;width:1200px;height:96px;z-index:3;display:flex;align-items:center;padding:0 33px 0 53px}
.brand{display:flex;align-items:center;gap:12px;color:var(--white);font-weight:700;font-size:17px;letter-spacing:.04em;text-transform:uppercase}
.brand-mark{width:30px;height:30px;background:var(--blue);border-radius:4px}
.main-nav{display:flex;gap:30px;margin-left:auto;margin-right:34px;font-size:12.5px;font-weight:600;letter-spacing:.03em;color:var(--white);text-transform:uppercase}
.main-nav a{position:relative}
.main-nav a.active::after{content:"";position:absolute;left:50%;transform:translateX(-50%);bottom:-10px;width:22px;height:2px;background:var(--blue)}
.btn{display:inline-flex;align-items:center;justify-content:center;gap:14px;font-size:12.5px;font-weight:700;letter-spacing:.04em;text-transform:uppercase;border-radius:6px}
.btn-primary{background:var(--blue);color:var(--white)}
.btn-outline-light{border:1.5px solid rgba(255,255,255,.85);color:var(--white)}
.btn-outline-blue{border:1.5px solid var(--blue);color:var(--blue);background:var(--white)}
.btn-white{background:var(--white);color:var(--blue)}
.header-cta{width:130px;height:42px;border-radius:22px;font-size:12px}

/* Hero */
.hero{position:absolute;left:0;top:0;width:1200px;height:737px;background:linear-gradient(90deg,#0b1525 0%,#0f1d33 40%,#1a2c46 100%)}
.hero-photo{position:absolute;right:0;top:70px;width:620px;height:667px;background:radial-gradient(ellipse at 60% 45%,#6b5a3e 0%,#3a3f4a 30%,#1a2a42 65%,transparent 100%),linear-gradient(180deg,#1c2e4a 0%,#2a3548 55%,#1d2a1e 100%);-webkit-mask:linear-gradient(90deg,transparent 0%,#000 30%);mask:linear-gradient(90deg,transparent 0%,#000 30%)}
.hero-copy{position:absolute;left:71px;top:198px;width:560px;color:var(--white)}
.eyebrow{font-size:13.5px;font-weight:600;letter-spacing:.06em;text-transform:uppercase;color:var(--blue)}
.hero-copy .eyebrow{color:#3b82f6}
.hero-title{font-size:49px;line-height:1.12;font-weight:600;margin-top:17px;letter-spacing:-.01em}
.hero-text{font-size:15px;line-height:1.75;color:#d7dde7;margin-top:28px;width:430px}
.hero-actions{display:flex;gap:20px;margin-top:33px}
.hero-actions .btn{height:50px}

/* Feature strip */
.features{position:absolute;left:71px;top:669px;width:1058px;height:221px;background:var(--white);border-radius:8px;box-shadow:0 10px 30px rgba(15,27,45,.10);display:flex;padding:38px 0 0;z-index:2}
.feature{flex:1;padding:0 40px 0 53px;border-right:1px solid var(--line);height:146px}
.feature:last-child{border-right:0}
.feature svg{width:40px;height:40px;stroke:var(--blue);fill:none;stroke-width:1.6;stroke-linecap:round;stroke-linejoin:round}
.feature h3{font-size:16px;font-weight:600;margin-top:22px}
.feature p{font-size:13px;line-height:1.75;color:var(--muted);margin-top:10px}

/* About */
.about-copy{position:absolute;left:71px;top:976px;width:440px}
.section-title{font-size:48px;font-weight:600;line-height:1.17;letter-spacing:-.015em;margin-top:20px}
.rule{width:42px;height:2px;background:var(--blue)}
.about-copy .rule{margin-top:32px}
.about-copy p{font-size:15px;line-height:1.8;color:var(--body);margin-top:28px}
.about-copy p + p{margin-top:22px}
.about-copy .btn{width:241px;height:50px;margin-top:38px;font-size:12px}
.about-photo{position:absolute;left:570px;top:990px;width:559px;height:460px;border-radius:8px;background:linear-gradient(180deg,#6fa3dc 0%,#a9c9e8 35%,#b9b8ae 55%,#5d7a5e 75%,#3b5a74 100%)}
.stats{position:absolute;left:607px;top:1321px;width:493px;height:158px;background:var(--white);border-radius:8px;box-shadow:0 10px 30px rgba(15,27,45,.12);display:flex;padding:30px 0 0}
.stat{flex:1;padding-left:45px;border-right:1px solid var(--line);height:98px}
.stat:last-child{border-right:0}
.stat strong{display:block;font-size:30px;font-weight:500;color:var(--blue)}
.stat span{display:block;font-size:13px;line-height:1.7;color:var(--muted);margin-top:10px}

/* Services */
.services{position:absolute;left:0;top:1533px;width:1200px;height:600px;background:var(--soft);text-align:center}
.services .eyebrow{margin-top:42px;font-size:13px}
.services h2{font-size:36px;font-weight:600;line-height:1.35;margin:12px auto 0;width:700px;letter-spacing:-.01em}
.services .rule{margin:22px auto 0;width:22px;height:2px;background:#9fbbe8}
.service-grid{position:absolute;left:71px;top:222px;display:flex;gap:13px}
.service-card{width:201px;height:238px;background:var(--white);border-radius:8px;text-align:left;padding:30px 22px 0 24px;box-shadow:0 2px 10px rgba(15,27,45,.04)}
.service-card svg{width:42px;height:42px;stroke:var(--blue);fill:none;stroke-width:1.5;stroke-linecap:round;stroke-linejoin:round}
.service-card h3{font-size:17px;font-weight:600;line-height:1.5;margin-top:20px;min-height:51px;display:flex;align-items:center}
.service-card p{font-size:12.5px;line-height:1.75;color:var(--muted);margin-top:10px}
.services .btn{position:absolute;left:461px;top:502px;width:278px;height:55px;font-size:12px}

/* Testimonial */
.testimonial{position:absolute;left:0;top:2133px;width:1200px;height:364px;background:radial-gradient(ellipse at 50% 60%,#1b2c44 0%,#0f1b2d 70%);text-align:center;color:var(--white)}
.quote-mark{margin-top:52px;font-size:90px;line-height:1;color:var(--blue);font-weight:700;height:60px;font-family:Georgia,serif}
.testimonial blockquote{font-size:24px;font-style:italic;line-height:1.75;width:740px;margin:14px auto 0;color:#f1f4f8}
.testimonial cite{display:block;font-style:normal;font-size:14.5px;font-weight:500;letter-spacing:.05em;margin-top:14px;text-transform:uppercase}
.dots{display:flex;gap:9px;justify-content:center;margin-top:33px}
.dots span{width:10px;height:10px;border-radius:50%;background:#d5dae2}
.dots span:first-child{background:var(--blue)}

/* CTA */
.cta-band{position:absolute;left:0;top:2497px;width:1200px;height:139px;background:var(--blue);color:var(--white);display:flex;align-items:center;padding:0 119px}
.cta-band svg{width:54px;height:54px;stroke:var(--white);fill:none;stroke-width:2;stroke-linecap:round;stroke-linejoin:round}
.cta-text{margin-left:31px}
.cta-text h2{font-size:20px;font-weight:600}
.cta-text p{font-size:14px;color:#dbe7fb;margin-top:8px}
.cta-band .btn{margin-left:auto;width:216px;height:52px;font-size:12px}

/* Footer */
.site-footer{position:absolute;left:0;top:2636px;width:1200px;height:365px;background:var(--footer);color:#c9d0da}
.footer-brand{position:absolute;left:91px;top:45px;width:250px}
.footer-brand .brand{font-size:15px}
.footer-brand p{font-size:13.5px;line-height:1.7;margin-top:22px;width:230px}
.social{display:flex;gap:16px;margin-top:18px}
.social span{width:28px;height:28px;border-radius:50%;background:#2b3a52}
.footer-col{position:absolute;top:53px}
.footer-col h4{font-size:13px;font-weight:700;letter-spacing:.06em;color:var(--white);text-transform:uppercase}
.footer-col ul{list-style:none;margin-top:26px}
.footer-col li{font-size:13.5px;line-height:30.5px;color:#e3e7ee}
.col-links{left:425px}
.col-resources{left:623px}
.col-contact{left:840px}
.contact-item{display:flex;gap:16px;font-size:13.5px;line-height:1.65;color:#e3e7ee;margin-top:0}
.contact-item svg{width:16px;height:16px;flex:none;margin-top:3px;fill:var(--white)}
.col-contact .contact-list{margin-top:26px;display:flex;flex-direction:column;gap:24px}
.footer-bottom{position:absolute;left:91px;top:292px;width:1018px;border-top:1px solid #283649;padding-top:24px;display:flex;font-size:13px}
.footer-bottom nav{margin-left:auto;display:flex;gap:22px;margin-right:6px}
</style>
</head>
<body>

<section class="hero">
  <div class="hero-photo" role="img" aria-label="Modern two-storey house lit warmly at dusk with trees behind"></div>
  <div class="hero-copy">
    <p class="eyebrow">Property management done right</p>
    <h1 class="hero-title">Protecting Your Property.<br>Maximizing Your<br>Investment.</h1>
    <p class="hero-text">Tallgrove Vale Management provides full-service property management solutions for residential and commercial properties across Ohio.</p>
    <div class="hero-actions">
      <a class="btn btn-primary" style="width:185px">Our Services
        <svg width="18" height="12" viewBox="0 0 18 12" fill="none" stroke="#fff" stroke-width="1.8" stroke-linecap="round" stroke-linejoin="round"><path d="M1 6h15M11 1l5 5-5 5"/></svg></a>
      <a class="btn btn-outline-light" style="width:179px">Get a Free Quote</a>
    </div>
  </div>
</section>

<header class="site-header">
  <a class="brand"><span class="brand-mark"></span>Tallgrove Vale Management</a>
  <nav class="main-nav">
    <a class="active">Home</a><a>Owners</a><a>Tenants</a><a>Services</a><a>About</a><a>Resources</a><a>Contact</a>
  </nav>
  <a class="btn btn-primary header-cta">Get a Quote</a>
</header>

<section class="features">
  <div class="feature">
    <svg viewBox="0 0 40 40"><path d="M20 4l13 5v10c0 9-6 15-13 18C13 34 7 28 7 19V9z"/><path d="M20 14v10M15.5 20l4.5 4.5 4.5-4.5"/></svg>
    <h3>Reliable &amp; Trusted</h3>
    <p>Local expertise you can<br>count on.</p>
  </div>
  <div class="feature">
    <svg viewBox="0 0 40 40"><path d="M5 34h30M8 34V24h5v10M17 34V20h5v10M26 34V16h5v18"/><circle cx="11" cy="18" r="1.5"/><circle cx="20" cy="14" r="1.5"/><circle cx="29" cy="9" r="1.5"/></svg>
    <h3>Maximize Returns</h3>
    <p>We minimize expenses and<br>maximize your ROI.</p>
  </div>
  <div class="feature">
    <svg viewBox="0 0 40 40"><circle cx="20" cy="13" r="7"/><path d="M6 35c1-8 7-12 14-12s13 4 14 12z"/></svg>
    <h3>Tenant Satisfaction</h3>
    <p>Happy tenants. Fewer<br>vacancies.</p>
  </div>
  <div class="feature">
    <svg viewBox="0 0 40 40"><circle cx="20" cy="20" r="15"/><path d="M20 11v10l6 4"/></svg>
    <h3>24/7 Support</h3>
    <p>We're here when you<br>need us.</p>
  </div>
</section>

<section class="about">
  <div class="about-copy">
    <p class="eyebrow">Who we are</p>
    <h2 class="section-title">Your Property.<br>Our Priority.</h2>
    <div class="rule"></div>
    <p>Tallgrove Vale Management is a full-service property management company dedicated to providing exceptional service, protecting your investment, and giving you peace of mind.</p>
    <p>With years of experience in the Ohio market, we handle the day-to-day so you can enjoy the returns.</p>
    <a class="btn btn-primary">Learn More About Us
      <svg width="18" height="12" viewBox="0 0 18 12" fill="none" stroke="#fff" stroke-width="1.8" stroke-linecap="round" stroke-linejoin="round"><path d="M1 6h15M11 1l5 5-5 5"/></svg></a>
  </div>
  <div class="about-photo" role="img" aria-label="City skyline with towers beside a river and footbridge under blue sky"></div>
  <div class="stats">
    <div class="stat"><strong>250+</strong><span>Properties<br>Managed</span></div>
    <div class="stat"><strong>98%</strong><span>Occupancy<br>Rate</span></div>
    <div class="stat"><strong>15+</strong><span>Years of Local<br>Experience</span></div>
  </div>
</section>

<section class="services">
  <p class="eyebrow">Our Services</p>
  <h2>Comprehensive Property Management Solutions</h2>
  <div class="rule"></div>
  <div class="service-grid">
    <article class="service-card">
      <svg viewBox="0 0 42 42"><path d="M5 20L21 6l16 14M9 17v19h24V17"/><path d="M17 36V26h8v10"/></svg>
      <h3>Residential<br>Management</h3>
      <p>Single-family, multi-family and everything in between.</p>
    </article>
    <article class="service-card">
      <svg viewBox="0 0 42 42"><path d="M7 37V7h17v30M24 16h11v21M4 37h34"/><path d="M12 13h2M17 13h2M12 19h2M17 19h2M12 25h2M17 25h2M28 22h3M28 28h3"/></svg>
      <h3>Commercial<br>Management</h3>
      <p>Office, retail, industrial and mixed-use properties.</p>
    </article>
    <article class="service-card">
      <svg viewBox="0 0 42 42"><circle cx="21" cy="21" r="15"/><path d="M25 15.5c-1-1.5-2.5-2-4-2-2.5 0-4 1.3-4 3.2 0 4.6 8.5 2.6 8.5 7.5 0 2-1.8 3.3-4.5 3.3-1.8 0-3.4-.7-4.3-2.2M21 11v3M21 27v3"/></svg>
      <h3>Rent Collection</h3>
      <p>On-time rent collection and detailed financial reporting.</p>
    </article>
    <article class="service-card">
      <svg viewBox="0 0 42 42"><path d="M28 5a8 8 0 0 0-7 11L6 31a3 3 0 0 0 5 5l15-15a8 8 0 0 0 11-7l-5 3-4-2-1-4z"/></svg>
      <h3>Maintenance<br>&amp; Repairs</h3>
      <p>Reliable vendors and 24/7 maintenance coordination.</p>
    </article>
    <article class="service-card">
      <svg viewBox="0 0 42 42"><circle cx="16" cy="14" r="6"/><path d="M4 34c1-7 6-10 12-10s11 3 12 10"/><circle cx="29" cy="15" r="5"/><path d="M30 24c5 0 8 3 9 9"/></svg>
      <h3>Tenant<br>Screening</h3>
      <p>Thorough screening for quality, long-term tenants.</p>
    </article>
  </div>
  <a class="btn btn-outline-blue">View All Services
    <svg width="18" height="12" viewBox="0 0 18 12" fill="none" stroke="#1c6ae0" stroke-width="1.8" stroke-linecap="round" stroke-linejoin="round"><path d="M1 6h15M11 1l5 5-5 5"/></svg></a>
</section>

<section class="testimonial">
  <div class="quote-mark">&ldquo;</div>
  <blockquote>Tallgrove Vale Management has been a game changer for our rental properties. Their team is responsive, professional, and truly cares about both owners and tenants.</blockquote>
  <cite>– Dana R., Property Owner</cite>
  <div class="dots"><span></span><span></span><span></span></div>
</section>

<section class="cta-band">
  <svg viewBox="0 0 54 54"><rect x="4" y="8" width="40" height="36" rx="4"/><path d="M4 18h40M14 4v8M34 4v8"/><circle cx="40" cy="40" r="10" fill="#1c6ae0"/><path d="M40 35v5l3 2"/></svg>
  <div class="cta-text">
    <h2>Ready to Experience Hassle-Free Property Management?</h2>
    <p>Get your free quote today and see the difference.</p>
  </div>
  <a class="btn btn-white">Get a Free Quote
    <svg width="18" height="12" viewBox="0 0 18 12" fill="none" stroke="#1c6ae0" stroke-width="1.8" stroke-linecap="round" stroke-linejoin="round"><path d="M1 6h15M11 1l5 5-5 5"/></svg></a>
</section>

<footer class="site-footer">
  <div class="footer-brand">
    <a class="brand"><span class="brand-mark"></span>Tallgrove Vale</a>
    <p>Proudly serving property owners across Ohio with reliable, professional, and results-driven property management.</p>
    <div class="social"><span></span><span></span><span></span></div>
  </div>
  <div class="footer-col col-links">
    <h4>Quick Links</h4>
    <ul><li>Home</li><li>Owners</li><li>Tenants</li><li>Services</li><li>About Us</li><li>Contact</li></ul>
  </div>
  <div class="footer-col col-resources">
    <h4>Resources</h4>
    <ul><li>Blog</li><li>FAQs</li><li>Owner Portal</li><li>Tenant Portal</li><li>Maintenance Request</li></ul>
  </div>
  <div class="footer-col col-contact">
    <h4>Contact Us</h4>
    <div class="contact-list">
      <div class="contact-item"><svg viewBox="0 0 16 16"><path d="M8 0a5.5 5.5 0 0 0-5.5 5.5C2.5 10 8 16 8 16s5.5-6 5.5-10.5A5.5 5.5 0 0 0 8 0zm0 7.6a2.1 2.1 0 1 1 0-4.2 2.1 2.1 0 0 1 0 4.2z"/></svg><span>1820 Linden Ridge Dr, Suite B<br>Westbrook, Ohio 43099</span></div>
      <div class="contact-item"><svg viewBox="0 0 16 16"><path d="M3.6 1l2.3 3-1.4 1.8a9 9 0 0 0 5.7 5.7L12 10.1l3 2.3-1.3 2.6C7.5 15 1 8.5 1 2.3z"/></svg><span>(614) 555-0187</span></div>
      <div class="contact-item"><svg viewBox="0 0 16 16"><path d="M1 3h14v10H1zm1.5 1.3V5l5.5 4 5.5-4v-.7z"/></svg><span>info@tallgrovevalemanagement.com</span></div>
    </div>
  </div>
  <div class="footer-bottom">
    <span>© 2024 Tallgrove Vale Management. All Rights Reserved.</span>
    <nav><a>Privacy Policy</a><span>|</span><a>Terms of Service</a></nav>
  </div>
</footer>

</body>
</html>
```